Lotus Leaf Kitchen Road Billboard

Road Billboard I need all of this information on it
Authentic Thai Food Bangkok Style
6.5 Miles on the right
4126 Maple Ridge Rd Otto NC
828-555-4172

```html
<!DOCTYPE html>
<html lang="en">
<head>
<meta charset="utf-8">
<title>Lotus Leaf Kitchen Road Billboard</title>
<link rel="stylesheet" href="https://fonts.googleapis.com/css2?family=Montserrat:wght@600;800&family=Metamorphous&display=swap">
<style>
  :root {
    --ink: #141005;
    --gold: #d8a915;
    --white: #ffffff;
    --chili: #bf4426;
    --basil: #487513;
    --plate-light: #d9dde6;
    --plate-shrimp: #d7754f;
  }
  html, body {
    margin: 0;
    width: 1200px;
    height: 735px;
    overflow: hidden;
    background: var(--white);
  }
  .canvas {
    position: relative;
    width: 1200px;
    height: 735px;
  }
  .billboard-shapes {
    position: absolute;
    left: 0;
    top: 0;
  }
  .text {
    position: absolute;
    margin: 0;
    white-space: nowrap;
    line-height: 1;
  }
  .brand-name {
    left: 270px;
    top: 304px;
    width: 154px;
    text-align: center;
    font-family: "Metamorphous", serif;
    font-size: 15px;
    color: var(--gold);
  }
  .distance {
    left: 496px;
    top: 238px;
    width: 228px;
    text-align: center;
    font-family: "Montserrat", sans-serif;
    font-weight: 800;
    font-size: 49px;
    letter-spacing: -1px;
    color: var(--white);
  }
  .direction {
    left: 496px;
    top: 289px;
    width: 228px;
    text-align: center;
    font-family: "Montserrat", sans-serif;
    font-weight: 800;
    font-size: 24px;
    color: var(--white);
  }
  .headline {
    left: 200px;
    top: 364px;
    font-family: "Metamorphous", serif;
    font-size: 40px;
    color: var(--ink);
  }
  .subline {
    left: 248px;
    top: 429px;
    font-family: "Metamorphous", serif;
    font-size: 36px;
    color: var(--gold);
  }
  .phone {
    left: 224px;
    top: 472px;
    font-family: "Montserrat", sans-serif;
    font-weight: 600;
    font-size: 33px;
    color: var(--white);
  }
  .address {
    left: 482px;
    top: 484px;
    font-family: "Montserrat", sans-serif;
    font-weight: 600;
    font-size: 18px;
    color: var(--white);
  }
</style>
</head>
<body>
<div class="canvas">
  <svg class="billboard-shapes" width="1200" height="735" viewBox="0 0 1200 735">
    <defs>
      <radialGradient id="dish-tones" cx="50%" cy="48%" r="55%">
        <stop offset="0" stop-color="var(--plate-shrimp)"/>
        <stop offset="0.55" stop-color="#c98a6e"/>
        <stop offset="1" stop-color="var(--plate-light)"/>
      </radialGradient>
    </defs>
    <rect class="board-base" x="189" y="216" width="729" height="303" fill="var(--ink)"/>
    <rect class="accent-chili" x="918" y="216" width="126" height="94" fill="var(--chili)"/>
    <rect class="accent-basil" x="918" y="397" width="126" height="122" fill="var(--basil)"/>
    <circle class="brand-dot" cx="346" cy="272" r="18" fill="var(--gold)"/>
    <polygon class="direction-arrow" points="185,347 589,347 589,317 713,388 589,459 589,428 185,428" fill="var(--gold)"/>
    <path class="map-pin" d="M655.5 436 a11.5 11.5 0 0 1 11.5 11.5 c0 8 -11.5 21.5 -11.5 21.5 s-11.5 -13.5 -11.5 -21.5 a11.5 11.5 0 0 1 11.5 -11.5 z M655.5 442.5 a4.5 4.5 0 1 0 0.01 0 z" fill="var(--gold)" fill-rule="evenodd"/>
    <circle class="dish-frame" cx="884" cy="368" r="157" fill="var(--white)"/>
    <circle class="dish-photo" cx="884" cy="368" r="149" fill="url(#dish-tones)" role="img" aria-label="Photo of a plate of stir-fried shrimp with basil, sliced tomato and lettuce"/>
  </svg>

  <p class="text brand-name">Lotus Leaf Kitchen</p>
  <p class="text distance">6.5 Miles</p>
  <p class="text direction">on the right</p>
  <p class="text headline">Authentic Thai Food</p>
  <p class="text subline">Bangkok Style</p>
  <p class="text phone">828-555-4172</p>
  <p class="text address">4126 Maple Ridge Rd Otto NC</p>
</div>
</body>
</html>
```